Bref créative
Modern Real Estate Design
Modern Real Estate Business cards
Modern
Derek Ashworth
Team Leader/Realtor
4816 N Birchwood Plaza Suite 300
Larkfield, UT, 84990
ashworthderek385@mailnest.example
derekashworthteam.example
I would like the card to be teal,white and grey. Also want to get design for presentation
folders. I have a sample of what I want it to look like that I can email if possible.
This is the style I'm looking for I made this and would like the cards and folders to use this look. Thanks
This is my logo. I will also need to put Summit 48 logo in the bottom corner of the card.
I need the S48 logo on card but not on anything else. Thanks

```html
<!DOCTYPE html>
<html lang="en">
<head>
<meta charset="utf-8">
<title>Derek Ashworth Team – Business Card</title>
<link href="https://fonts.googleapis.com/css2?family=Open+Sans:wght@400;600&display=swap" rel="stylesheet">
<style>
  :root {
    --teal: #1aa7a5;
    --teal-dark: #128a89;
    --grey: #8d8f92;
    --grey-light: #c4c6c8;
    --ink: #4a4c4f;
    --paper: #ffffff;
    --backdrop: #e6e7e8;
  }
  * { margin: 0; padding: 0; box-sizing: border-box; }
  html, body {
    width: 1200px; height: 984px; overflow: hidden;
    background: var(--backdrop);
    font-family: "Open Sans", Arial, sans-serif;
    color: var(--ink);
  }
  .sheet {
    width: 1200px; height: 984px;
    display: flex; flex-direction: column; align-items: center;
    justify-content: center; gap: 36px;
  }
  .card {
    position: relative;
    width: 760px; height: 434px;
    background: var(--paper);
    border-radius: 26px;
    overflow: hidden;
    box-shadow: 0 6px 18px rgba(0,0,0,.12);
  }
  .card-swooshes { position: absolute; left: 0; top: 0; width: 760px; height: 434px; }

  /* back side */
  .brand-center {
    position: absolute; inset: 0;
    display: flex; align-items: center; justify-content: center; gap: 14px;
  }
  .brand-mark { width: 30px; height: 30px; background: var(--teal); flex: none; }
  .brand-name {
    font-weight: 600; font-size: 30px; letter-spacing: 3px;
    color: var(--teal); text-transform: uppercase; white-space: nowrap;
  }

  /* front side */
  .front-brand {
    position: absolute; left: 40px; top: 170px; width: 340px;
    text-align: center;
  }
  .front-brand .brand-row { display: flex; align-items: center; justify-content: center; gap: 10px; }
  .front-brand .brand-mark { width: 20px; height: 20px; }
  .front-brand .brand-name { font-size: 21px; letter-spacing: 1.5px; }
  .brand-url { margin-top: 8px; font-size: 13px; color: var(--grey); letter-spacing: .5px; }
  .divider {
    position: absolute; left: 400px; top: 110px; width: 2px; height: 220px;
    background: var(--grey-light);
  }
  .contact { position: absolute; left: 428px; top: 112px; width: 300px; }
  .contact-name { font-weight: 600; font-size: 19px; color: var(--teal); }
  .contact-title { font-size: 13px; color: var(--grey); margin-bottom: 14px; }
  .contact-list { list-style: none; }
  .contact-list li {
    display: flex; align-items: center; gap: 8px;
    font-size: 11.5px; line-height: 21px; color: var(--ink); white-space: nowrap;
  }
  .contact-list li.indent { padding-left: 22px; }
  .icon { width: 14px; height: 14px; flex: none; }
</style>
</head>
<body>
<main class="sheet">

  <section class="card card-back" aria-label="Business card back">
    <svg class="card-swooshes" viewBox="0 0 760 434" aria-hidden="true">
      <path d="M0 0 H170 L0 130 Z" fill="var(--grey)"/>
      <path d="M760 0 H590 L760 130 Z" fill="var(--grey)"/>
      <path d="M0 434 H170 L0 304 Z" fill="var(--teal)"/>
      <path d="M760 434 H590 L760 304 Z" fill="var(--teal)"/>
      <rect x="0" y="0" width="760" height="434" rx="150" ry="115" fill="var(--paper)"/>
    </svg>
    <div class="brand-center">
      <span class="brand-mark"></span>
      <span class="brand-name">Derek Ashworth Team</span>
    </div>
  </section>

  <section class="card card-front" aria-label="Business card front">
    <svg class="card-swooshes" viewBox="0 0 760 434" aria-hidden="true">
      <path d="M0 0 H170 L0 130 Z" fill="var(--teal)"/>
      <path d="M760 0 H590 L760 130 Z" fill="var(--teal)"/>
      <path d="M760 434 H590 L760 304 Z" fill="var(--teal)"/>
      <path d="M0 434 H170 L0 304 Z" fill="var(--grey-light)"/>
      <rect x="0" y="0" width="760" height="434" rx="150" ry="115" fill="var(--paper)"/>
    </svg>

    <div class="front-brand">
      <div class="brand-row">
        <span class="brand-mark"></span>
        <span class="brand-name">Derek Ashworth Team</span>
      </div>
      <div class="brand-url">derekashworthteam.example</div>
    </div>

    <div class="divider"></div>

    <div class="contact">
      <div class="contact-name">Derek Ashworth</div>
      <div class="contact-title">Team Leader/Realtor</div>
      <ul class="contact-list">
        <li>
          <svg class="icon" viewBox="0 0 14 14"><circle cx="7" cy="7" r="7" fill="var(--teal)"/><path d="M7 3.2a2.3 2.3 0 0 0-2.3 2.3C4.7 7.3 7 10.5 7 10.5s2.3-3.2 2.3-5A2.3 2.3 0 0 0 7 3.2z" fill="#fff"/></svg>
          4816 N Birchwood Plaza Suite 300
        </li>
        <li class="indent">Larkfield, UT, 84990</li>
        <li>
          <svg class="icon" viewBox="0 0 14 14"><circle cx="7" cy="7" r="7" fill="var(--teal)"/><path d="M4.6 3.6l1.3-.3.7 1.7-.8.6a4.5 4.5 0 0 0 2.6 2.6l.6-.8 1.7.7-.3 1.3c-3.3.3-6.1-2.5-5.8-5.8z" fill="#fff"/></svg>
          801-555-0134
        </li>
        <li>
          <svg class="icon" viewBox="0 0 14 14"><circle cx="7" cy="7" r="7" fill="var(--teal)"/><path d="M4.6 3.6l1.3-.3.7 1.7-.8.6a4.5 4.5 0 0 0 2.6 2.6l.6-.8 1.7.7-.3 1.3c-3.3.3-6.1-2.5-5.8-5.8z" fill="#fff"/></svg>
          801-555-0178
        </li>
        <li>
          <svg class="icon" viewBox="0 0 14 14"><circle cx="7" cy="7" r="7" fill="var(--teal)"/><path d="M4.6 3.6l1.3-.3.7 1.7-.8.6a4.5 4.5 0 0 0 2.6 2.6l.6-.8 1.7.7-.3 1.3c-3.3.3-6.1-2.5-5.8-5.8z" fill="#fff"/></svg>
          888-555-0192
        </li>
        <li>
          <svg class="icon" viewBox="0 0 14 14"><circle cx="7" cy="7" r="7" fill="var(--teal)"/><rect x="3.6" y="4.6" width="6.8" height="4.8" fill="#fff"/><path d="M3.6 4.6L7 7.3l3.4-2.7" fill="none" stroke="var(--teal)" stroke-width=".8"/></svg>
          ashworthderek385@mailnest.example
        </li>
        <li>
          <svg class="icon" viewBox="0 0 14 14"><circle cx="7" cy="7" r="7" fill="var(--teal)"/><circle cx="7" cy="7" r="3.4" fill="none" stroke="#fff" stroke-width=".9"/><path d="M3.6 7h6.8M7 3.6v6.8" stroke="#fff" stroke-width=".8"/></svg>
          www.derekashworthteam.example
        </li>
      </ul>
    </div>
  </section>

</main>
</body>
</html>
```